Infographics for Quorvel reports

Quorvel report is a summary of software developer skills.

Main purpose of our reports is to provide quick and easy insight into skill set of tested individual.
Our mission is to help talents to stand out.

Our target market is a male between 25-40, bit of a nerd, who likes technology and computer games.
The report should communicate quality and trust.

Report should fit on one A4 page and contain the following
1. Company logo - provided with the brief

2. Information about tested developer:
- Photo of developer
- Full name
- Location
- Email

3. How he or she compares against the average Software Developer:
- Collaboration ranking (0-100)
- Skills ranking by languages (up to 10 languages)

4. Total ranking - Number 1-100% which should stand out as a quick reference

We would like to included some sort of stamp of approval on the report.
The stamp would contain the overall score of a developer (The Total ranking from point 4.) .

As an option we were considering to use some sort of categorisation for the total ranking.
Here are examples of Quorvel categories:
Wizard of Quorvel for ranking between 90% – 100%
Scholar of Quorvel for ranking between 80% - 89%
Knight of Quorvel for ranking between 70% - 79%
Warrior of Quorvel for ranking between 60% - 69%
Rebel of Quorvel unknown or under 60%

Developer would belong to one of the categories depending on their Total ranking.

We are not very fixed on category names. We would be happy to consider any other option.

Here are some example data for the report:

The average Software Developer ranking is 50%.

Tested Developer:
Photo
Full name: Mark Tester
Location: Sydney, Australia
Email: mark.tester@mailvex.com

Collaboration ranking: 95%

Skills:
Language: C++
Number of Open Source Projects: 5
Ranking: 91%

Language: Javascript
Number of Open Source Projects: 3
Ranking: 81%

Language: Python
Number of Open Source Projects: 1
Ranking: 31%

Language: Ruby
Number of Open Source Projects: 2
Ranking: 25%

Language: C#
Ranking: 85%

Language: Java
Ranking: 75%

Total Ranking: 75% - Knight of Quorvel

Thank you!

```html
<!DOCTYPE html>
<html lang="en">
<head>
<meta charset="utf-8">
<title>Quorvel – Software Developer Skills</title>
<link rel="stylesheet" href="https://fonts.googleapis.com/css2?family=Alfa+Slab+One&family=Oswald:wght@500;600;700&family=Roboto:wght@400;700&display=swap">
<style>
  :root{
    --purple:#9b2a7c;
    --purple-dark:#6e1a57;
    --grey:#a7a9ac;
    --ink:#231f20;
    --paper:#ffffff;
    --stripe-a:#d6d6d8;
    --stripe-b:#cbcbce;
    --ribbon-grey:#8e8e91;
  }
  *{box-sizing:border-box;margin:0;padding:0}
  html,body{width:848px;height:1200px;overflow:hidden}
  body{
    position:relative;
    font-family:"Roboto",Arial,sans-serif;
    color:var(--ink);
    background:repeating-linear-gradient(90deg,var(--stripe-a) 0 26px,var(--stripe-b) 26px 52px);
  }
  .abs{position:absolute}

  /* header */
  .side-ribbon{position:absolute;top:45px;width:150px;height:120px;background:var(--ribbon-grey);opacity:.75}
  .side-ribbon.left{left:0;clip-path:polygon(0 0,100% 20%,100% 100%,0 80%,18% 40%)}
  .side-ribbon.right{right:0;clip-path:polygon(0 20%,100% 0,82% 40%,100% 80%,0 100%)}
  .brand{position:absolute;top:14px;left:0;width:848px;display:flex;justify-content:center;align-items:center;gap:10px}
  .brand-mark{width:30px;height:30px;background:var(--purple)}
  .brand-name{font-family:"Oswald",sans-serif;font-weight:600;font-size:38px;line-height:1;color:var(--ink)}
  .title-banner{position:absolute;left:97px;top:78px;width:653px;height:137px;background:#000;
    display:flex;align-items:center;justify-content:center;text-align:center}
  .title-banner h1{font-family:"Alfa Slab One",serif;font-weight:400;color:#fff;font-size:45px;line-height:1.13;letter-spacing:.5px}

  /* profile card */
  .profile{position:absolute;left:28px;top:245px;width:796px;height:282px;background:var(--paper);overflow:hidden;
    box-shadow:0 2px 4px rgba(0,0,0,.15)}
  .tested-ribbon{position:absolute;left:-62px;top:80px;width:300px;height:46px;background:var(--purple);transform:rotate(-45deg);
    color:#fff;font-family:"Oswald",sans-serif;font-weight:600;font-size:22px;display:flex;align-items:center;justify-content:center;letter-spacing:.5px}
  .contact{position:absolute;left:56px;top:164px;list-style:none}
  .contact li{display:flex;align-items:center;height:34px;font-size:25px}
  .contact svg{width:26px;height:26px;margin-right:20px;fill:var(--purple)}
  .contact .name{font-weight:700}
  .stamp{position:absolute;left:388px;top:58px;width:162px;height:162px;border-radius:50%;
    background:radial-gradient(circle,var(--purple) 0 30%,#fff 31% 54%,var(--purple) 55% 100%);opacity:.85}
  .photo-frame{position:absolute;left:540px;top:18px;width:200px;height:242px;border:6px solid var(--purple);border-radius:28px;background:#fff}

  /* skills */
  .panel{position:absolute;top:543px;height:629px;background:var(--paper);box-shadow:0 2px 4px rgba(0,0,0,.15)}
  .skills{left:28px;width:590px}
  .skills h2{position:absolute;left:14px;top:10px;font-family:"Oswald",sans-serif;font-weight:600;font-size:27px;color:var(--purple)}
  .col-head{position:absolute;top:60px;font-family:"Oswald",sans-serif;font-weight:500;font-size:16px}
  .skill-row{position:absolute;left:14px;width:562px;height:89px;display:flex;align-items:center}
  .skill-row + .skill-row{border-top:1px dashed var(--grey)}
  .file-icon{width:74px;height:74px;margin-left:6px}
  .projects{display:flex;gap:15px;margin-left:32px;width:330px}
  .projects svg{width:50px;height:58px}
  .rank{font-family:"Alfa Slab One",serif;font-size:46px;color:var(--purple);margin-left:auto;margin-right:10px}

  /* summary */
  .summary{left:634px;width:190px}
  .gauge{position:absolute;left:40px;width:112px;height:112px}
  .gauge-value{position:absolute;left:40px;width:112px;text-align:center;font-family:"Oswald",sans-serif;font-weight:600;font-size:27px;color:var(--purple)}
  .gauge-label{position:absolute;left:0;width:190px;text-align:center;font-family:"Oswald",sans-serif;font-weight:500;font-size:16px;line-height:22px}
  .divider{position:absolute;left:10px;width:170px;border-top:1px dashed var(--grey)}
  .band{position:absolute;left:-6px;width:202px;height:30px;background:var(--purple);color:#fff;
    font-family:"Oswald",sans-serif;font-weight:600;font-size:18px;display:flex;align-items:center;justify-content:center;letter-spacing:.5px}
  .band::before,.band::after{content:"";position:absolute;bottom:-6px;border-top:6px solid var(--purple-dark)}
  .band::before{left:0;border-left:6px solid transparent}
  .band::after{right:0;border-right:6px solid transparent}
</style>
</head>
<body>
<svg width="0" height="0" style="position:absolute">
  <defs>
    <symbol id="clipboard" viewBox="0 0 50 58">
      <rect x="2" y="6" width="38" height="44" rx="4" fill="#a7a9ac"/>
      <rect x="7" y="11" width="28" height="35" fill="#fff"/>
      <rect x="13" y="2" width="16" height="8" rx="2" fill="#9b2a7c"/>
      <rect x="11" y="17" width="18" height="2.5" fill="#231f20"/>
      <rect x="11" y="23" width="18" height="2.5" fill="#231f20"/>
      <rect x="11" y="29" width="14" height="2.5" fill="#231f20"/>
      <rect x="11" y="35" width="10" height="2.5" fill="#231f20"/>
      <circle cx="38" cy="46" r="11" fill="#9b2a7c" stroke="#fff" stroke-width="2"/>
      <path d="M33 46l4 4 7-8" fill="none" stroke="#fff" stroke-width="3"/>
    </symbol>
    <symbol id="file" viewBox="0 0 74 74">
      <path d="M6 0h36l18 18v56H6z" fill="#231f20"/>
      <path d="M42 0v18h18" fill="#fff" opacity=".35"/>
    </symbol>
  </defs>
</svg>

<div class="side-ribbon left"></div>
<div class="side-ribbon right"></div>

<header class="brand">
  <span class="brand-mark"></span>
  <span class="brand-name">Quorvel</span>
</header>
<div class="title-banner"><h1>SOFTWARE<br>DEVELOPER SKILLS</h1></div>

<section class="profile">
  <div class="tested-ribbon">TESTED DEVELOPER</div>
  <ul class="contact">
    <li class="name"><svg viewBox="0 0 24 24"><circle cx="12" cy="7" r="5"/><path d="M3 24c0-7 4-10 9-10s9 3 9 10z"/></svg>MARK TESTER</li>
    <li><svg viewBox="0 0 24 24"><path d="M12 0a8 8 0 0 0-8 8c0 6 8 16 8 16s8-10 8-16a8 8 0 0 0-8-8zm0 11a3 3 0 1 1 0-6 3 3 0 0 1 0 6z"/></svg>Sydney, Australia</li>
    <li><svg viewBox="0 0 24 24"><path d="M0 4h24v3L12 14 0 7z"/><path d="M0 9l12 7 12-7v11H0z"/></svg>mark.tester@mailvex.com</li>
  </ul>
  <div class="stamp" role="img" aria-label="Approved stamp with star"></div>
  <div class="photo-frame" role="img" aria-label="Developer photo"></div>
</section>

<section class="panel skills">
  <h2>SKILLS RANKING BY LANGUAGES</h2>
  <span class="col-head" style="left:14px">LANGUAGE</span>
  <span class="col-head" style="left:172px">OPEN SOURCE PROJECTS</span>
  <span class="col-head" style="left:482px">RANKING</span>

  <div class="skill-row" style="top:94px">
    <svg class="file-icon" viewBox="0 0 74 74"><use href="#file"/><rect x="14" y="34" width="58" height="26" rx="6" fill="#9b2a7c"/><text x="43" y="53" text-anchor="middle" fill="#fff" font-family="Oswald,sans-serif" font-size="17">C++</text></svg>
    <div class="projects"><svg><use href="#clipboard"/></svg><svg><use href="#clipboard"/></svg><svg><use href="#clipboard"/></svg><svg><use href="#clipboard"/></svg><svg><use href="#clipboard"/></svg></div>
    <span class="rank">91%</span>
  </div>
  <div class="skill-row" style="top:183px">
    <svg class="file-icon" viewBox="0 0 74 74"><use href="#file"/><rect x="14" y="34" width="58" height="26" rx="6" fill="#9b2a7c"/><text x="43" y="53" text-anchor="middle" fill="#fff" font-family="Oswald,sans-serif" font-size="17">JPS</text></svg>
    <div class="projects"><svg><use href="#clipboard"/></svg><svg><use href="#clipboard"/></svg><svg><use href="#clipboard"/></svg></div>
    <span class="rank">81%</span>
  </div>
  <div class="skill-row" style="top:272px">
    <svg class="file-icon" viewBox="0 0 74 74"><use href="#file"/><rect x="14" y="34" width="58" height="26" rx="6" fill="#9b2a7c"/><text x="43" y="53" text-anchor="middle" fill="#fff" font-family="Oswald,sans-serif" font-size="17">PY</text></svg>
    <div class="projects"><svg><use href="#clipboard"/></svg></div>
    <span class="rank">31%</span>
  </div>
  <div class="skill-row" style="top:361px">
    <svg class="file-icon" viewBox="0 0 74 74"><use href="#file"/><rect x="14" y="34" width="58" height="26" rx="6" fill="#9b2a7c"/><text x="43" y="53" text-anchor="middle" fill="#fff" font-family="Oswald,sans-serif" font-size="17">RUBY</text></svg>
    <div class="projects"><svg><use href="#clipboard"/></svg><svg><use href="#clipboard"/></svg></div>
    <span class="rank">25%</span>
  </div>
  <div class="skill-row" style="top:450px">
    <svg class="file-icon" viewBox="0 0 74 74"><use href="#file"/><rect x="14" y="34" width="58" height="26" rx="6" fill="#9b2a7c"/><text x="43" y="53" text-anchor="middle" fill="#fff" font-family="Oswald,sans-serif" font-size="17">C#</text></svg>
    <div class="projects"><svg><use href="#clipboard"/></svg><svg><use href="#clipboard"/></svg><svg><use href="#clipboard"/></svg></div>
    <span class="rank">85%</span>
  </div>
  <div class="skill-row" style="top:539px">
    <svg class="file-icon" viewBox="0 0 74 74"><use href="#file"/><rect x="14" y="34" width="58" height="26" rx="6" fill="#9b2a7c"/><text x="43" y="53" text-anchor="middle" fill="#fff" font-family="Oswald,sans-serif" font-size="17">JAR</text></svg>
    <div class="projects"><svg><use href="#clipboard"/></svg><svg><use href="#clipboard"/></svg><svg><use href="#clipboard"/></svg><svg><use href="#clipboard"/></svg><svg><use href="#clipboard"/></svg></div>
    <span class="rank">75%</span>
  </div>
</section>

<aside class="panel summary">
  <svg class="gauge" style="top:21px" viewBox="0 0 112 112"><circle cx="56" cy="56" r="50" fill="none" stroke="#a7a9ac" stroke-width="9"/><circle cx="56" cy="56" r="50" fill="none" stroke="#9b2a7c" stroke-width="9" stroke-dasharray="157 314" transform="rotate(-90 56 56)"/></svg>
  <span class="gauge-value" style="top:57px">50%</span>
  <p class="gauge-label" style="top:144px">SOFTWARE<br>DEVELOPER RANKING</p>
  <div class="divider" style="top:195px"></div>

  <svg class="gauge" style="top:221px" viewBox="0 0 112 112"><circle cx="56" cy="56" r="50" fill="none" stroke="#a7a9ac" stroke-width="9"/><circle cx="56" cy="56" r="50" fill="none" stroke="#9b2a7c" stroke-width="9" stroke-dasharray="298 314" transform="rotate(-90 56 56)"/></svg>
  <span class="gauge-value" style="top:257px">95%</span>
  <p class="gauge-label" style="top:343px">COLLABORATION<br>RANKING</p>
  <div class="divider" style="top:395px"></div>

  <div class="band" style="top:414px">TOTAL RANKING</div>
  <svg class="gauge" style="top:463px" viewBox="0 0 112 112"><circle cx="56" cy="56" r="50" fill="none" stroke="#a7a9ac" stroke-width="9"/><circle cx="56" cy="56" r="50" fill="none" stroke="#9b2a7c" stroke-width="9" stroke-dasharray="236 314" transform="rotate(-90 56 56)"/></svg>
  <span class="gauge-value" style="top:499px">75%</span>
  <div class="band" style="top:592px">KNIGHT OF QUORVEL</div>
</aside>
</body>
</html>
```